Gerald Pinnock - Corporate MC & Entertainer

Design a one page A4 flyer
(See Brief Attached)
I'm after a one Page Flyer
A4 Size - One sided
I want the finished artwork in 2 Forms.
1/ One that I could print out myself in a small run ( I have a Dorvan Tint PrintMaster)
or send out as a PDF
2/ A second version that could be printed commercially , so including bleed crop marks so it can be cut to A4 size
I have attached the copy that should be included. (Agency Sweep 2014 WORDS)
If there was too much text to include , we could drop one of the testimonial quotes
I have attached 3 images that could be included if there is room.
If there were too many images I suggest dropping Image 3 ( with bow tie)
As you can see from the copy (or a visit to my website) there are two main services that I provide
Corporate MC Services and Entertainment Services.
These are however intertwined - My MC work often includes some entertaining effects from my ThoughtCatcher Show. I often get booked to MC a conference and provide a show.
I'm after something that is -
Classy , Sophisticated, Smart, perhaps a bit quirky.
Nothing "Magic" like - eg no Rabbits , Wands, puffs of smoke
I have no corporate colour or logo or branding that should be included
You can see some previous flyers here http://www.proflinkora.com/in/geraldpinnock
I like these, but looking for new ideas
Target Market(s)
Corporate , Conference Organisers, Speaker Bureau owners, Large Association Conference committees
Industry/Entity Type
Entertainment
Colors
Designer to choose colors to be used in the design.

```html
<!DOCTYPE html>
<html lang="en">
<head>
<meta charset="utf-8">
<title>Gerald Pinnock – Corporate MC &amp; Entertainer</title>
<link rel="stylesheet" href="https://fonts.googleapis.com/css2?family=Alfa+Slab+One&family=Marcellus&family=Gelasio:wght@400;500&display=swap">
<style>
  :root {
    --navy: #0a2a86;
    --royal: #1a5ec8;
    --deep: #29498c;
    --mist: #dfe5ef;
    --mist-dark: #c5cfdf;
    --flame: #ec3a1c;
    --ink: #1a1a1a;
    --white: #ffffff;
  }
  * { margin: 0; padding: 0; box-sizing: border-box; }
  html, body { width: 944px; height: 1200px; overflow: hidden; background: #ffffff; }
  .flyer {
    position: relative;
    width: 944px;
    height: 1200px;
    overflow: hidden;
    background: linear-gradient(180deg, #f4f6fa 0px, #e6ebf3 330px, #b9c6dc 470px, #7d95c0 640px, #4a6aa6 860px, var(--deep) 1200px);
  }
  .portrait {
    position: absolute;
    left: 10px; top: 10px;
    width: 484px; height: 356px;
    background: radial-gradient(ellipse at 45% 40%, #e8dcd4 0%, #c9b8ae 35%, #5a5a62 70%, #2a2a30 100%);
  }
  .divider {
    position: absolute;
    left: 494px; top: 10px;
    width: 6px; height: 356px;
    background: var(--navy);
  }
  .name {
    position: absolute;
    font-family: "Alfa Slab One", Georgia, serif;
    line-height: 1;
    -webkit-text-stroke: 3px var(--white);
    paint-order: stroke fill;
    text-shadow: 4px 5px 5px rgba(0,0,0,0.45);
  }
  .name-first { left: 362px; top: 24px; font-size: 118px; color: var(--royal); }
  .name-last { left: 528px; top: 170px; font-size: 88px; color: var(--navy); }
  .name-rule {
    position: absolute;
    left: 758px; top: 150px;
    width: 136px; height: 3px;
    background: var(--navy);
  }
  .band {
    position: absolute;
    left: 10px; width: 924px;
  }
  .band-tagline {
    top: 366px; height: 88px;
    background: linear-gradient(180deg, #ffffff 0%, #f3f5f9 100%);
  }
  .tagline {
    position: absolute; left: 30px; top: 14px;
    font-family: "Gelasio", Georgia, serif;
    font-size: 49px; color: var(--flame);
  }
  .band-role {
    top: 456px; height: 66px;
    background: linear-gradient(180deg, #f7f8fb 0%, #e4e9f1 100%);
  }
  .role {
    position: absolute; left: 40px; top: 8px;
    font-family: "Marcellus", Georgia, serif;
    font-size: 44px; color: var(--ink);
  }
  .band-promise {
    top: 538px; height: 58px;
    background: linear-gradient(180deg, #eef1f6 0%, #d6deea 100%);
  }
  .promise {
    position: absolute; left: 40px; top: 12px;
    font-family: "Marcellus", Georgia, serif;
    font-size: 29px; color: var(--ink);
  }
  .content {
    position: absolute;
    left: 26px; top: 612px; width: 880px;
    font-family: "Gelasio", Georgia, serif;
    font-size: 20px; line-height: 26px;
    color: var(--white);
  }
  .highlights { list-style: none; }
  .highlights li { position: relative; padding-left: 26px; margin-bottom: 0; }
  .highlights li::before {
    content: "";
    position: absolute; left: 4px; top: 8px;
    width: 10px; height: 10px;
    background: var(--white);
    clip-path: polygon(25% 0, 75% 0, 100% 50%, 75% 100%, 25% 100%, 0 50%);
  }
  .plain { padding-left: 26px; }
  .gap { margin-top: 26px; }
  .site { word-spacing: 8px; }
  .quote .source { white-space: nowrap; }
</style>
</head>
<body>
<main class="flyer">
  <div class="portrait" role="img" aria-label="Portrait photo of Gerald Pinnock smiling, grey hair and glasses, dark jacket"></div>
  <div class="divider"></div>

  <h1>
    <span class="name name-first">Gerald</span>
    <span class="name name-last">Pinnock</span>
  </h1>
  <div class="name-rule"></div>

  <div class="band band-tagline"><p class="tagline">“Australias Magician of the mind”</p></div>
  <div class="band band-role"><h2 class="role">Corporate MC &amp; Entertainer</h2></div>
  <div class="band band-promise"><p class="promise">Solving your Conference Puzzles!</p></div>

  <section class="content">
    <ul class="highlights">
      <li>In the last two years Gerald has been engaged as the Conference MC for events in Hawaii, New Zealand, Hong Kong &amp; all States of Australia.</li>
      <li>He facilitated 24 Australian Major Project Conferences for FairVista and 16 International CEO Summits for Summitline Global.</li>
      <li>In the Australian Corporate Sector, he managed major events for &nbsp;- OzCover Brokers, BRNA, CareNest, Signal Hire, ParishCare and the Seedling &amp; Grove Association.</li>
      <li>As an Entertainer he cruised the world on several luxury cruise ships, visiting Japan, Korea, China, Tahiti and New Zealand in his travels.</li>
    </ul>
    <p class="plain gap">What's coming up in 2014?</p>
    <p class="plain gap site">Get involved at &nbsp;http://www.GeraldPinnock.com</p>
    <p class="plain gap">Recent Testimonials</p>
    <p class="plain gap quote">"A big thank you for a really good job on Friday night which was carried out with aplomb - well done!" &nbsp;- Seedling &amp; Grove Association</p>
    <p class="plain gap quote">"Huge thanks for your professionalism with the Awards, getting a laugh from everyone and in general creating an atmosphere that was enjoyable and relaxed!" &nbsp;- &nbsp;<span class="source">CareNest</span></p>
  </section>
</main>
</body>
</html>
```